Modern solo law firm website

I am preparing to launch a solo law practice (I own the domain farrowcounsel.com and/or may use Farrow Law Office as a dba), and will need to move quickly to put up a website once I pull the trigger. There are many existing law firm sites to "copy," but I'm looking for something a little more modern and unique with some scrolling and modern icons (see e.g., brintelaw.com). Right now, need the logo and skeleton for the site, as I have not written all of the content. For now, I like the idea of a simple home page that incorporates the phrase "Impactful. Valuable. Trusted." (Again, I may change that text.) And would like links on the home page across the top for "about", "services", "people" and "contact" -- these should lead to separate landing pages. The bottom of the home page also should have a link for a "disclaimer" and to Facebook, Twitter and LinkedIn (which I have not yet created). Make sense? Let me know if you have questions.

Target Market(s)

Business clients

Industry/Entity Type

Law Firm

Number of Pages Required

5+ page

Font styles to use
Other font styles liked:
• Perhaps Segoe UI

Requirements
Must have
• DRAFT STRUCTURE AND TEXT NOW ATTACHED. HOWEVER, SUBJECT TO EDITS BEING MADE CONCURRENTLY.

```html
<!DOCTYPE html>
<html lang="en">
<head>
<meta charset="utf-8">
<title>Farrow Legal — Services</title>
<link rel="stylesheet" href="https://fonts.googleapis.com/css2?family=Open+Sans:wght@300;400;600&display=swap">
<style>
:root{
  --ink:#111d24;
  --nav:#555b60;
  --nav-active:#2aa7d6;
  --brand:#1f78b8;
  --social:#1592d6;
  --hero-teal:#2e8fa3;
  --hero-mist:#9eb0ad;
  --hero-sub:#a8e6f4;
  --band:#2a9aa8;
  --panel:#4e9ea5;
  --panel-light:#5aa6ab;
  --icon-fill:#2ba3ab;
  --icon-ring:#7fd0d2;
  --list:#eaf6f7;
  --footer:#042638;
  --footer-text:#e6f1f5;
  --footer-logo:#a7c9db;
  --button:#4b97a8;
  --button-ring:#9cd3e0;
}
*{box-sizing:border-box;margin:0;padding:0}
html,body{width:1181px;height:1200px;overflow:hidden}
body{font-family:"Open Sans",sans-serif;background:var(--panel);position:relative;color:var(--ink)}

.site-header{position:absolute;left:0;top:0;width:1181px;height:85px;background:linear-gradient(#ffffff,#e9e9e9);border-bottom:1px solid #d8d8d8}
.brand-name{position:absolute;left:99px;top:24px;font-size:33px;font-weight:400;color:var(--brand);letter-spacing:-0.3px}
.main-nav{position:absolute;left:673px;top:36px;display:flex}
.main-nav a{font-size:15px;color:var(--nav);text-decoration:none;margin-right:34px}
.main-nav a.is-active{color:var(--nav-active)}
.social-links{position:absolute;left:1007px;top:36px;display:flex;gap:4px}
.social-links span{display:block;width:22px;height:21px;background:var(--social)}

.hero{position:absolute;left:0;top:86px;width:1181px;height:338px;
  background:
   radial-gradient(ellipse 420px 300px at 1050px 300px,var(--hero-mist),transparent 70%),
   radial-gradient(ellipse 520px 260px at 520px 80px,#3aa1ad,transparent 75%),
   radial-gradient(ellipse 600px 320px at 100px 330px,#06223e,transparent 75%),
   linear-gradient(100deg,#0e4866 0%,var(--hero-teal) 55%,#6aa9ab 100%)}
.hero-title{position:absolute;left:98px;top:122px;font-size:56px;font-weight:400;color:#fff;letter-spacing:-0.5px}
.hero-sub{position:absolute;left:97px;top:196px;font-size:17px;font-weight:400;color:var(--hero-sub)}
.hero-band{position:absolute;left:0;top:424px;width:1181px;height:7px;background:var(--band);border-top:1px solid #bfe8ec}

.services{position:absolute;left:0;top:431px;width:1181px;height:674px;
  background:radial-gradient(ellipse 500px 400px at 200px 200px,var(--panel-light),transparent 80%),linear-gradient(110deg,#55a2a7,#4a97a4)}
.services-heading{position:absolute;left:100px;top:37px;font-size:21px;font-weight:400;color:#fff}

.service{position:absolute;top:102px}
.service-icon{position:absolute;width:72px;height:72px;border-radius:50%;background:var(--icon-fill);border:2px solid var(--icon-ring)}
.service-icon svg{position:absolute;left:18px;top:18px}
.service-title{position:absolute;top:97px;font-size:16px;font-weight:400;color:var(--ink);white-space:nowrap}
.service-list{position:absolute;top:130px;list-style:none;width:230px}
.service-list li{position:relative;padding-left:18px;font-size:12px;line-height:21px;color:var(--list);letter-spacing:.2px;margin-bottom:16px}
.service-list li::before{content:"";position:absolute;left:0;top:7px;width:7px;height:7px;border:1.5px solid var(--list);border-radius:50%}
.service-list.tight li{line-height:16px;margin-bottom:25px}
.service-list.tight li::before{top:4px}

.site-footer{position:absolute;left:0;top:1105px;width:1181px;height:95px;background:var(--footer);border-top:1px solid #7fb5c0}
.footer-brand{position:absolute;left:101px;top:26px;font-size:23px;font-weight:400;color:var(--footer-logo)}
.footer-address,.footer-contact{position:absolute;font-style:normal;font-size:13px;line-height:22px;color:var(--footer-text)}
.footer-address{left:416px;top:27px}
.footer-contact{left:533px;top:25px}
.cta{position:absolute;left:806px;top:29px;width:239px;height:34px;border-radius:17px;background:var(--button);border:2px solid var(--button-ring);color:#fff;font-size:16px;text-align:center;line-height:30px;text-decoration:none}
</style>
</head>
<body>
<header class="site-header">
  <div class="brand-name">Farrow Legal</div>
  <nav class="main-nav">
    <a href="#">about</a><a href="#" class="is-active">services</a><a href="#">people</a><a href="#">contact</a>
  </nav>
  <div class="social-links"><span aria-label="Social profile 1"></span><span aria-label="Social profile 2"></span><span aria-label="Social profile 3"></span></div>
</header>

<section class="hero">
  <h1 class="hero-title">Mr. Farrow has advised</h1>
  <p class="hero-sub">Clients across a broad variety of industries and business and legal matters.</p>
</section>
<div class="hero-band"></div>

<main class="services">
  <h2 class="services-heading">Areas where Farrow Legal can help your company include:</h2>

  <div class="service" style="left:110px">
    <div class="service-icon" style="left:55px">
      <svg width="32" height="32" viewBox="0 0 32 32"><circle cx="16" cy="9" r="6" fill="#fff"/><path d="M4 27c0-7 5-10 12-10s12 3 12 10z" fill="#fff"/></svg>
    </div>
    <h3 class="service-title" style="left:1px">Outside general counsel.</h3>
    <ul class="service-list tight" style="left:-4px">
      <li>Regular interaction with your business and key decisionmakers</li>
      <li>Strategic advisor for day-to-day legal affairs</li>
      <li>Commercial contracts, licensing agreements and strategic transactions</li>
      <li>Document review</li>
      <li>Human Resources matters</li>
      <li style="line-height:20px">Proactive identification and preventive mitigation of legal exposures and risk</li>
      <li>Managespecialized outside counsel, including their bills</li>
    </ul>
  </div>

  <div class="service" style="left:362px">
    <div class="service-icon" style="left:80px">
      <svg width="32" height="32" viewBox="0 0 32 32"><rect x="5" y="3" width="22" height="26" rx="3" fill="#fff"/><g stroke="#2ba3ab" stroke-width="2"><line x1="9" y1="10" x2="20" y2="10"/><line x1="9" y1="14" x2="20" y2="14"/><line x1="9" y1="18" x2="20" y2="18"/><line x1="9" y1="22" x2="20" y2="22"/></g></svg>
    </div>
    <h3 class="service-title" style="left:0">Litigation and dispute resolution.</h3>
    <ul class="service-list" style="left:10px;width:200px">
      <li>General commercial litigation</li>
      <li>Antitrust and business competition</li>
      <li>Breach of contract</li>
      <li>Digital privacy and advertising</li>
      <li>Employment</li>
      <li>Insurance coverage</li>
      <li>Intellectual property and technology</li>
      <li>Non-compete and non-disclosure</li>
    </ul>
  </div>

  <div class="service" style="left:643px">
    <div class="service-icon" style="left:52px">
      <svg width="32" height="32" viewBox="0 0 32 32"><circle cx="16" cy="8" r="6" fill="#fff"/><path d="M3 28c0-7 5-11 13-11s13 4 13 11z" fill="#fff"/><path d="M14 17h4l-1 3 2 7h-6l2-7z" fill="#1b6f80"/></svg>
    </div>
    <h3 class="service-title" style="left:0">Employment consulting.</h3>
    <ul class="service-list" style="left:0;width:180px">
      <li>Employment counseling</li>
      <li>New employee hiring and retention</li>
      <li>NDA and non-compete agreements</li>
      <li>Policies and handbooks</li>
      <li>Separations</li>
    </ul>
  </div>

  <div class="service" style="left:874px">
    <div class="service-icon" style="left:74px">
      <svg width="32" height="32" viewBox="0 0 32 32"><rect x="4" y="9" width="24" height="18" rx="4" fill="#fff"/><path d="M12 9V6h8v3" fill="none" stroke="#fff" stroke-width="2.5"/><line x1="4" y1="16" x2="28" y2="16" stroke="#1b6f80" stroke-width="2"/></svg>
    </div>
    <h3 class="service-title" style="left:41px">Business documents.</h3>
    <ul class="service-list" style="left:0;width:250px">
      <li>Contract drafting and review</li>
      <li>Vendor and supplyservice agreements</li>
      <li>IP agreements (licensing, NDA)</li>
      <li style="width:210px">Real estate purchase and commercial lease agreements</li>
      <li>Business organization documents</li>
    </ul>
  </div>
</main>

<footer class="site-footer">
  <div class="footer-brand">Farrowlegal</div>
  <address class="footer-address">Farrow Legal<br>418 Linden Ave.</address>
  <address class="footer-contact">Maplewood, IL 60299<br>555-014-2280<br>info@farrowcounsel.com</address>
  <a class="cta" href="#">Get in Touch</a>
</footer>
</body>
</html>
```